professional looking data specialist website

I've recently had a new logo designed and I'm now looking to get a professional looking website built. This is for a new company that specialises in data. We look to support companies with business intelligence, report modelling, data governance to new european legislation (GDPR). We are offer consultancy or we can attend site and complete work when required. Our target arket is united kingdom wide and we are specifically aiming at small to medium sized companies.

Target Market(s)

small to medium enterprise companies from all industries

Industry/Entity Type

Professional Service

Coding

Coded - Design and coding required

Number of Pages Required

4 page

Font styles to use
Sans Serif

Colors

Designer to choose colors to be used in the design.

Requirements
Must have
• Professional look including the company logo, need to have ability to request more information from us so needs a inquiries page, seperate pages for the different offerings, data governance, report modelling, business intelligence implementation, data protection
Nice to have
• any website interaction, animation, etc
Should not have
• too many colours, too busy pages, must look professional

```html
<!DOCTYPE html>
<html lang="en">
<head>
<meta charset="utf-8">
<title>Harlow Data Ltd</title>
<link rel="stylesheet" href="https://fonts.googleapis.com/css2?family=Cabin:wght@500;600;700&family=Lato:wght@400;700&display=swap">
<style>
:root{
  --blue:#1a6fc0;
  --blue-bar:#1766b2;
  --ink:#555555;
  --ink-dark:#3d3d3d;
  --grey-band:#eeeeee;
  --grey-foot:#5b5b5b;
  --muted:#8a8a8a;
  --white:#ffffff;
}
*{box-sizing:border-box;margin:0;padding:0}
html,body{width:728px;height:1200px;overflow:hidden;background:var(--white)}
body{position:relative;font-family:'Lato',sans-serif;color:var(--ink)}
.abs{position:absolute}
.heading{font-family:'Cabin',sans-serif;font-weight:600}

/* header */
.site-header{left:0;top:0;width:728px;height:82px}
.brand{left:50px;top:12px;display:flex;align-items:center;gap:8px}
.brand-mark{width:14px;height:14px;background:var(--blue)}
.brand-name{font-family:'Cabin',sans-serif;font-weight:600;font-size:17px;color:var(--blue)}
.top-contact{top:14px;font-size:8px;color:var(--ink);display:flex;align-items:center;gap:6px}
.top-contact .ico{width:18px;height:18px;border:1px solid #9a9a9a;border-radius:2px;display:flex;align-items:center;justify-content:center}
.nav{top:59px;font-family:'Cabin',sans-serif;font-weight:600;font-size:10.5px;color:var(--ink-dark)}
.nav.active{color:var(--blue)}
.nav-sep{top:60px;width:1px;height:8px;background:#ddd}
.nav-marker{left:402px;top:40px;width:10px;height:10px;background:var(--blue)}

/* hero */
.hero{left:0;top:82px;width:728px;height:305px;background:radial-gradient(ellipse at 40% 45%,#3aa6d8 0%,#1c5f8c 30%,#10304a 65%,#0b1b2a 100%)}
.hero-caption-bar{left:0;top:343px;width:728px;height:44px;background:rgba(10,20,30,.55)}
.hero-caption{left:0;top:347px;width:728px;text-align:center;color:var(--white);font-family:'Cabin',sans-serif;font-weight:600;font-size:14px;line-height:17px}
.hero-arrow{top:205px;width:24px;height:23px;background:#3a3a3a;border:1px solid #888;display:flex;align-items:center;justify-content:center}

/* welcome */
.section-title{left:0;width:728px;text-align:center;font-family:'Cabin',sans-serif;font-weight:600;font-size:20px;color:var(--ink)}
.section-title span,.left-title span{color:var(--blue)}
.rule{height:1px;width:50px;background:#aaa}
.welcome-text{left:54px;top:454px;width:620px;text-align:center;font-size:8.4px;line-height:13.7px;color:#333}
.btn{left:329px;top:521px;width:70px;height:21px;background:#8c8c8c;border-radius:2px;color:var(--white);font-family:'Cabin',sans-serif;font-size:9px;display:flex;align-items:center;justify-content:center}

/* services */
.services-band{left:0;top:570px;width:728px;height:280px;background:var(--grey-band)}
.service{top:650px;width:150px;text-align:center}
.service-icon{width:72px;height:72px;margin:0 auto;position:relative}
.service-title{margin-top:16px;font-family:'Cabin',sans-serif;font-weight:600;font-size:12px;line-height:14px;color:var(--blue)}
.service-text{margin-top:6px;font-size:8.3px;line-height:12px;color:var(--muted)}
.service-plus{width:15px;height:15px;margin:9px auto 0;background:#9a9a9a;color:var(--white);font-size:13px;line-height:15px;font-weight:700}

/* commitment */
.left-title{left:49px;top:877px;font-family:'Cabin',sans-serif;font-weight:600;font-size:19.5px;color:var(--ink)}
.commit-text{left:49px;top:918px;width:310px;font-size:9.6px;line-height:15.6px;color:#333}
.commit-list{left:49px;top:973px;list-style:none;font-size:9.6px;color:#333}
.commit-list li{display:flex;align-items:center;gap:7px;height:22px}
.photo-frame{left:399px;top:882px;width:276px;height:190px;border:1.5px solid var(--blue);border-top:none;border-right:none}
.photo{left:405px;top:883px;width:274px;height:185px;background:linear-gradient(135deg,#3e5068 0%,#9ab0c4 45%,#e6d3c2 55%,#6c8aa8 75%,#2e4058 100%)}

/* footer */
.footer-bar{left:0;top:1086px;width:728px;height:43px;background:var(--blue-bar)}
.footer-links{left:50px;top:1100px;color:var(--white);font-size:10.5px;display:flex;gap:12px}
.social{top:1097px;width:20px;height:20px;border:1.3px solid var(--white);border-radius:2px}
.footer-base{left:0;top:1129px;width:728px;height:71px;background:var(--grey-foot);color:var(--white)}
.foot-item{top:1152px;display:flex;gap:8px;font-size:8.3px;line-height:14px}
.foot-item b{font-weight:700}
.foot-ico{width:19px;height:19px;border:1px solid #ccc;border-radius:2px;display:flex;align-items:center;justify-content:center;margin-top:2px}
.copyright{left:540px;top:1155px;width:140px;text-align:right;font-size:8px;line-height:11px}
</style>
</head>
<body>

<header class="abs site-header">
  <div class="abs brand"><span class="brand-mark"></span><span class="brand-name">Harlow Data Ltd</span></div>

  <div class="abs top-contact" style="left:488px">
    <span class="ico"><svg width="10" height="10" viewBox="0 0 10 10"><path d="M2 1l2 2-1 1.2c.6 1.3 1.5 2.2 2.8 2.8L7 6l2 2-1.3 1.3C4.5 9 1 5.5.7 2.3z" fill="#1a6fc0"/></svg></span>
    (020)-555-0142
  </div>
  <div class="abs top-contact" style="left:581px">
    <span class="ico"><svg width="10" height="8" viewBox="0 0 10 8"><rect x="0.5" y="0.5" width="9" height="7" rx="1" fill="#1a6fc0"/><path d="M1 1l4 3 4-3" stroke="#fff" fill="none"/></svg></span>
    info@harlowdata.example
  </div>

  <div class="abs nav-marker"></div>
  <nav>
    <span class="abs nav active" style="left:394px">Home</span>
    <span class="abs nav-sep" style="left:442px"></span>
    <span class="abs nav" style="left:463px">About Us</span>
    <span class="abs nav-sep" style="left:526px"></span>
    <span class="abs nav" style="left:546px">Services</span>
    <span class="abs nav-sep" style="left:606px"></span>
    <span class="abs nav" style="left:626px">Contact Us</span>
  </nav>
</header>

<section>
  <div class="abs hero" role="img" aria-label="Hand holding glowing blue technology icons in front of server racks"></div>
  <div class="abs hero-caption-bar"></div>
  <p class="abs hero-caption">Offering Consultancy Services From Small To Medium Enterprises<br>Companies To All Industries In The UK</p>
  <div class="abs hero-arrow" style="left:3px"><svg width="8" height="10" viewBox="0 0 8 10"><path d="M6 1L2 5l4 4" stroke="#fff" stroke-width="2" fill="none"/></svg></div>
  <div class="abs hero-arrow" style="left:701px"><svg width="8" height="10" viewBox="0 0 8 10"><path d="M2 1l4 4-4 4" stroke="#fff" stroke-width="2" fill="none"/></svg></div>
</section>

<section>
  <h1 class="abs section-title" style="top:404px">Welcome To <span>Harlow Data</span> Ltd</h1>
  <div class="abs rule" style="left:339px;top:439px"></div>
  <p class="abs welcome-text">Lorem ipsum dolor sit amet, consectetuer adipiscing elit, sed diam nonummy nibh euismod tincidunt ut laoreet dolore magna aliquam erat volutpat. Ut wisi enim ad minim veniam, quis nostrud exerci tation ullamcorper suscipit lobortis nisl ut aliquip ex ea commodo consequat. Duis autem vel eum iriure dolor in hendrerit in vulputate velit esse molestie consequat, vel illum dolore eu feugiat nulla facilisis at vero eros et accumsan et iusto odio dignissim qui blandit praesent luptatum zzril delenit augue duis dolore te feugait nulla facilisi euismod tincidunt ut laoreet dolore magna aliquam.</p>
  <div class="abs btn">Read More</div>
</section>

<section>
  <div class="abs services-band"></div>
  <h2 class="abs section-title" style="top:590px">Our <span>Services</span></h2>
  <div class="abs rule" style="left:339px;top:625px"></div>

  <div class="abs service" style="left:46px">
    <div class="service-icon"><svg width="72" height="72" viewBox="0 0 72 72"><path d="M20 2H2v68h68V50" stroke="#8a8a8a" stroke-width="4" fill="none"/><rect x="20" y="22" width="18" height="7" rx="1.5" fill="#1a6fc0"/><rect x="20" y="31" width="18" height="7" rx="1.5" fill="#1a6fc0"/><rect x="20" y="40" width="18" height="7" rx="1.5" fill="#1a6fc0"/><circle cx="45" cy="38" r="8" fill="none" stroke="#1a6fc0" stroke-width="3"/></svg></div>
    <div class="service-title">Data<br>Governance</div>
    <p class="service-text">Lorem ipsum dolor sit amet, consectetuer adipiscing elit, sed diam nonummy nibh euismod tincidu.</p>
    <div class="service-plus">+</div>
  </div>

  <div class="abs service" style="left:208px">
    <div class="service-icon"><svg width="72" height="72" viewBox="0 0 72 72"><path d="M20 2H2v68h68V50" stroke="#8a8a8a" stroke-width="4" fill="none"/><rect x="24" y="18" width="24" height="34" fill="none" stroke="#1a6fc0" stroke-width="2"/><path d="M29 26h14M29 32h14M29 38h14M29 44h14" stroke="#1a6fc0" stroke-width="2.5"/></svg></div>
    <div class="service-title">Report<br>Modeling</div>
    <p class="service-text">Lorem ipsum dolor sit amet, consectetuer adipiscing elit, sed diam nonummy nibh euismod tincidu.</p>
    <div class="service-plus">+</div>
  </div>

  <div class="abs service" style="left:371px">
    <div class="service-icon"><svg width="72" height="72" viewBox="0 0 72 72"><path d="M20 2H2v68h68V50" stroke="#8a8a8a" stroke-width="4" fill="none"/><path d="M21 52V44h5v8zM29 52V38h5v14zM37 52V40h5v12zM45 52V30h5v22z" fill="#1a6fc0"/><path d="M20 40l10-9 7 4 13-13" stroke="#1a6fc0" stroke-width="3" fill="none"/><path d="M45 20h8v8z" fill="#1a6fc0"/></svg></div>
    <div class="service-title">Business Intelligence<br>Implementation</div>
    <p class="service-text">Lorem ipsum dolor sit amet, consectetuer adipiscing elit, sed diam nonummy nibh euismod tincidu.</p>
    <div class="service-plus">+</div>
  </div>

  <div class="abs service" style="left:533px">
    <div class="service-icon"><svg width="72" height="72" viewBox="0 0 72 72"><path d="M20 2H2v68h68V50" stroke="#8a8a8a" stroke-width="4" fill="none"/><ellipse cx="34" cy="22" rx="12" ry="4" fill="#1a6fc0"/><path d="M22 26c0 3 24 3 24 0v6c0 3-24 3-24 0zM22 35c0 3 24 3 24 0v6c0 3-24 3-24 0z" fill="#1a6fc0"/><circle cx="46" cy="44" r="7" fill="#1a6fc0" stroke="#eee" stroke-width="2"/><rect x="43" y="43" width="6" height="5" fill="#fff"/></svg></div>
    <div class="service-title">Data<br>Protection</div>
    <p class="service-text">Lorem ipsum dolor sit amet, consectetuer adipiscing elit, sed diam nonummy nibh euismod tincidu.</p>
    <div class="service-plus">+</div>
  </div>
</section>

<section>
  <h2 class="abs left-title">Our <span>Commitment To Customers</span></h2>
  <div class="abs rule" style="left:49px;top:907px;width:44px"></div>
  <p class="abs commit-text">Loren  autem vel eum iriure hendrerit in vulputate velit esse molestie. onsectetuer adipiscing elit, sed diam nonummy nibh euismod tincidunt u eu feugiat nulla facilisis.</p>
  <ul class="abs commit-list">
    <li><svg width="9" height="9" viewBox="0 0 9 9"><circle cx="4.5" cy="4.5" r="4.5" fill="#1a6fc0"/><path d="M2.3 4.6l1.5 1.4 3-3" stroke="#fff" stroke-width="1.2" fill="none"/></svg>Autem vel eum iriure hendrerit in</li>
    <li><svg width="9" height="9" viewBox="0 0 9 9"><circle cx="4.5" cy="4.5" r="4.5" fill="#1a6fc0"/><path d="M2.3 4.6l1.5 1.4 3-3" stroke="#fff" stroke-width="1.2" fill="none"/></svg>Gendrerit in vulputate velit</li>
    <li><svg width="9" height="9" viewBox="0 0 9 9"><circle cx="4.5" cy="4.5" r="4.5" fill="#1a6fc0"/><path d="M2.3 4.6l1.5 1.4 3-3" stroke="#fff" stroke-width="1.2" fill="none"/></svg>Autem vel eum adipiscing elit, sed diam</li>
    <li><svg width="9" height="9" viewBox="0 0 9 9"><circle cx="4.5" cy="4.5" r="4.5" fill="#1a6fc0"/><path d="M2.3 4.6l1.5 1.4 3-3" stroke="#fff" stroke-width="1.2" fill="none"/></svg>Eeum iriure hendrerit in vulputate velit</li>
  </ul>
  <div class="abs photo-frame"></div>
  <div class="abs photo" role="img" aria-label="Two business people in suits shaking hands"></div>
</section>

<footer>
  <div class="abs footer-bar"></div>
  <nav class="abs footer-links"><span>Home</span><span>|</span><span>About Us</span><span>|</span><span>Services</span><span>|</span><span>Contact Us</span></nav>
  <span class="abs social" style="left:579px"></span>
  <span class="abs social" style="left:606px"></span>
  <span class="abs social" style="left:633px"></span>
  <span class="abs social" style="left:660px"></span>

  <div class="abs footer-base"></div>
  <div class="abs foot-item" style="left:49px">
    <span class="foot-ico"><svg width="8" height="11" viewBox="0 0 8 11"><path d="M4 10.5S.5 6.5.5 4a3.5 3.5 0 017 0c0 2.5-3.5 6.5-3.5 6.5z" fill="none" stroke="#fff"/><circle cx="4" cy="4" r="1.2" fill="#fff"/></svg></span>
    <div><b>Harlow Data Ltd</b><br>45, Mill Lane, Kettering - NN16 0AA</div>
  </div>
  <div class="abs foot-item" style="left:278px">
    <span class="foot-ico"><svg width="10" height="10" viewBox="0 0 10 10"><path d="M2 1l2 2-1 1.2c.6 1.3 1.5 2.2 2.8 2.8L7 6l2 2-1.3 1.3C4.5 9 1 5.5.7 2.3z" fill="none" stroke="#fff"/></svg></span>
    <div><b>Call Us :</b><br>(020)-555-0142</div>
  </div>
  <div class="abs foot-item" style="left:409px">
    <span class="foot-ico"><svg width="11" height="8" viewBox="0 0 11 8"><rect x="0.5" y="0.5" width="10" height="7" fill="none" stroke="#fff"/><path d="M1 1l4.5 3.5L10 1" stroke="#fff" fill="none"/></svg></span>
    <div><b>Email Us :</b><br>info@harlowdata.example</div>
  </div>
  <p class="abs copyright">Copyright © 2017 Harlow Data Ltd.<br>All Rights Reserved.</p>
</footer>

</body>
</html>
```